Optometry need some pictures for business card

I am interested in getting the 3 pictures below in minimum 300dpi created as close as possible to the original image for our businesss sized magnets. Cannot be exactly same due to copyright. I have added details of our logo on new image uploaded and content that needs to be magnet. If you can present all 3 cards with seperate images in the one file that would be excellent.
Thank you

Please try and replicate all 3 images as close as possible with minimum 300 dpi. No writing required at all only images. If 3 images are too big for card size doesn't matter as I can use for 3 different cards. Thank you

```html
<!DOCTYPE html>
<html lang="en">
<head>
<meta charset="utf-8">
<title>Optometry Business Card</title>
<link rel="stylesheet" href="https://fonts.googleapis.com/css2?family=Tinos:wght@400;700&family=Arimo:wght@400&display=swap">
<style>
  :root {
    --backdrop: #e9e5de;
    --card-purple: #2e2068;
    --photo-light: #ece6e2;
    --photo-mid: #d9cfcb;
    --photo-pink: #e9b3c8;
    --tagline-ink: #2a1f63;
    --text-white: #ffffff;
  }
  * { margin: 0; padding: 0; box-sizing: border-box; }
  html, body {
    width: 1200px;
    height: 870px;
    overflow: hidden;
    background: var(--backdrop);
  }
  .canvas {
    position: relative;
    width: 1200px;
    height: 870px;
  }
  .business-card {
    position: absolute;
    left: 380px;
    top: 50px;
    width: 440px;
    height: 770px;
    overflow: hidden;
    background: var(--card-purple);
    box-shadow: 0 6px 18px rgba(0, 0, 0, 0.18);
  }
  .card-art {
    position: absolute;
    inset: 0;
    width: 440px;
    height: 770px;
  }
  .tagline {
    position: absolute;
    top: 34px;
    right: 22px;
    font-family: "Tinos", "Times New Roman", serif;
    font-weight: 700;
    font-size: 27px;
    color: var(--tagline-ink);
    -webkit-text-stroke: 0;
    text-shadow:
      2px 0 0 var(--text-white), -2px 0 0 var(--text-white),
      0 2px 0 var(--text-white), 0 -2px 0 var(--text-white),
      2px 2px 0 var(--text-white), -2px -2px 0 var(--text-white),
      2px -2px 0 var(--text-white), -2px 2px 0 var(--text-white);
  }
  .contact-block {
    position: absolute;
    left: 0;
    right: 0;
    top: 520px;
    text-align: center;
    color: var(--text-white);
  }
  .doctor-name {
    font-family: "Tinos", "Times New Roman", serif;
    font-size: 35px;
    font-weight: 400;
    margin-bottom: 12px;
  }
  .contact-line {
    font-family: "Arimo", Arial, sans-serif;
    font-size: 27px;
    line-height: 40px;
  }
</style>
</head>
<body>
<main class="canvas">
  <article class="business-card">
    <svg class="card-art" viewBox="0 0 440 770" xmlns="http://www.w3.org/2000/svg">
      <defs>
        <linearGradient id="photoTones" x1="0" y1="0" x2="1" y2="1">
          <stop offset="0" stop-color="var(--photo-light)"/>
          <stop offset="0.55" stop-color="var(--photo-mid)"/>
          <stop offset="1" stop-color="var(--photo-light)"/>
        </linearGradient>
        <radialGradient id="pinkGlow" cx="0.4" cy="0.45" r="0.45">
          <stop offset="0" stop-color="var(--photo-pink)" stop-opacity="0.55"/>
          <stop offset="1" stop-color="var(--photo-pink)" stop-opacity="0"/>
        </radialGradient>
      </defs>
      <g role="img" aria-label="Photo of a white puppy resting on a blanket wearing pink toy glasses">
        <rect x="0" y="0" width="440" height="480" fill="url(#photoTones)"/>
        <rect x="0" y="0" width="440" height="480" fill="url(#pinkGlow)"/>
      </g>
      <path class="purple-band" d="M0 465 Q 230 370 440 440 L440 770 L0 770 Z" fill="var(--card-purple)"/>
    </svg>
    <p class="tagline">See all that you can see !</p>
    <section class="contact-block">
      <h1 class="doctor-name">Dr.Dana Whitfield</h1>
      <p class="contact-line">2150 W. Larkspur</p>
      <p class="contact-line">Mesa, AZ 85201</p>
      <p class="contact-line">(480) 555-0147</p>
    </section>
  </article>
</main>
</body>
</html>
```